Pamphlet for IT Services Company (MSP Provider or Managed Services Provider)

We need a pamphlet designed for our Managed Services Company. We are an established company of 17 years that has never advertised. We'd like a pamphlet that we can drop off at potential client sites that describes our services. I like clean and prefer Orange as an accent color. We'd like to touch on the fact that we cater to our clients needs and go above and beyond what the other providers do.

Target Market(s)

Small and Medium Sized Businesses

Industry/Entity Type

It Service

Font styles to use
Other font styles liked:
• Try to match font on logo or website

Requirements
Must have
• Must highlight with the following Services and descriptions with Logo
Managed IT Services
IT Support
VOIP Solutions
WiFI Solutions
Contact information with phone number and website address.
Please view website korvanetpro.com
try to match fons on website above.
Nice to have
• Customer Testimonials. May a couple one line testimonials. Not real sure because this is the first time we've ever designed a brochure.
Should not have
• Not Sure

```html
<!DOCTYPE html>
<html lang="en">
<head>
<meta charset="utf-8">
<title>Korvanet Technologies – Managed IT Services Flyer</title>
<link rel="stylesheet" href="https://fonts.googleapis.com/css2?family=Ubuntu:ital,wght@0,300;0,400;0,500;0,700;1,400&family=Open+Sans:wght@400;600&display=swap">
<style>
  :root {
    --orange: #fb7410;
    --navy: #28313d;
    --slate: #3b4553;
    --ink: #2b2b2b;
    --grey: #d9dbde;
    --page: #ececec;
    --white: #ffffff;
  }
  * { box-sizing: border-box; margin: 0; padding: 0; }
  html, body { width: 1200px; height: 848px; overflow: hidden; }
  body { background: var(--page); font-family: "Open Sans", sans-serif; color: var(--ink); }

  .flyer {
    position: absolute; left: 310px; top: 14px;
    width: 580px; height: 820px;
    background: var(--white); overflow: hidden;
    box-shadow: 0 6px 22px rgba(0,0,0,.18);
  }

  .hero-photo {
    position: absolute; left: 0; top: 62px; width: 580px; height: 338px;
    background: linear-gradient(110deg, #27323d 0%, #5b6a77 30%, #b9c3cb 55%, #e3e8ec 75%, #9aa6b1 100%);
  }
  .hero-photo-strip {
    position: absolute; left: 0; top: 400px; width: 60px; height: 30px;
    background: linear-gradient(180deg, #4a5865, #7d8a95);
  }

  .header-shape { position: absolute; left: 0; top: 0; }

  .brand {
    position: absolute; left: 34px; top: 40px;
    display: flex; align-items: center; gap: 10px;
    font-family: "Ubuntu", sans-serif; font-weight: 300;
    font-size: 24px; color: var(--orange); letter-spacing: .2px;
  }
  .brand-dot { width: 22px; height: 22px; border: 2px solid var(--orange); border-radius: 50%; }

  .social { position: absolute; right: 40px; top: 18px; display: flex; gap: 10px; }
  .social span { width: 24px; height: 24px; border: 1.5px solid var(--white); border-radius: 50%; }

  .title-box {
    position: absolute; left: 60px; top: 300px; width: 440px; height: 118px;
    background: var(--navy); border-top-right-radius: 14px;
    padding: 18px 22px 0 26px;
  }
  .title-box::after {
    content: ""; position: absolute; left: 0; right: -6px; bottom: -4px; height: 4px;
    background: var(--orange);
  }
  .title-main {
    font-family: "Ubuntu", sans-serif; font-weight: 700; font-size: 34px;
    color: var(--orange); line-height: 1; white-space: nowrap;
  }
  .title-sub {
    font-family: "Ubuntu", sans-serif; font-size: 13px; color: var(--white);
    margin-top: 10px; white-space: nowrap;
  }
  .title-quote {
    font-family: "Ubuntu", sans-serif; font-style: italic; font-size: 13px;
    color: var(--orange); margin-top: 4px; white-space: nowrap;
  }

  .service { position: absolute; width: 262px; }
  .service-head { position: relative; height: 54px; }
  .service-icon {
    position: absolute; left: 0; top: 0; width: 54px; height: 54px; border-radius: 50%;
    background: var(--white); border: 4px solid var(--grey);
    box-shadow: 0 2px 4px rgba(0,0,0,.15);
    display: flex; align-items: center; justify-content: center; z-index: 2;
  }
  .service-pill {
    position: absolute; left: 38px; top: 11px; right: 0; height: 32px;
    background: var(--orange); border-radius: 0 16px 16px 0;
    padding-left: 26px; display: flex; align-items: center; white-space: nowrap;
    font-family: "Ubuntu", sans-serif; font-weight: 500; font-size: 16px; color: var(--white);
  }
  .service-text {
    margin: 4px 0 0 30px; font-size: 9.5px; line-height: 1.45; color: var(--ink);
  }

  .svc-managed { left: 24px; top: 440px; }
  .svc-support { left: 24px; top: 566px; }
  .svc-voip { left: 296px; top: 432px; }
  .svc-wifi { left: 296px; top: 600px; }

  .partners {
    position: absolute; left: 24px; right: 24px; top: 712px; height: 46px;
    border-top: 1px solid #9a9a9a;
    display: flex; align-items: center; justify-content: space-between;
    font-family: "Ubuntu", sans-serif; color: #4a4a4a; white-space: nowrap;
  }
  .partner { font-size: 11px; font-weight: 500; }
  .partner-major { font-size: 14px; font-weight: 400; color: var(--ink); }
  .partner-badge { width: 70px; height: 26px; background: #3a3a3a; }

  .contact-bar {
    position: absolute; left: 0; right: 0; bottom: 0; height: 58px;
    background: var(--orange);
    display: flex; align-items: center; justify-content: space-around;
    font-family: "Ubuntu", sans-serif; font-weight: 500; font-size: 14px; color: var(--white);
  }
  .contact-item { display: flex; align-items: center; gap: 7px; white-space: nowrap; }
  .contact-divider { width: 1px; height: 24px; background: rgba(255,255,255,.7); }
</style>
</head>
<body>
<main class="flyer">
  <div class="hero-photo" role="img" aria-label="Photo of an IT technician in a white shirt and tie touching floating device icons in front of server racks"></div>
  <div class="hero-photo-strip" role="img" aria-label="Continuation of the server room photo"></div>

  <svg class="header-shape" width="580" height="130" viewBox="0 0 580 130" aria-hidden="true">
    <rect x="330" y="0" width="250" height="62" fill="#3b4553"/>
    <path d="M0 0 H340 V62 Q340 108 296 112 L0 120 Z" fill="#ffffff"/>
    <path d="M340 58 Q340 108 296 112 L180 115" fill="none" stroke="#fb7410" stroke-width="4"/>
  </svg>

  <div class="brand"><span class="brand-dot"></span>korvanet technologies</div>
  <div class="social" aria-label="Social links"><span></span><span></span><span></span></div>

  <section class="title-box">
    <h1 class="title-main">Managed IT Services</h1>
    <p class="title-sub">A Simple, Cost Effective Plan for your IT Infrastructure.</p>
    <p class="title-quote">“Wouldn’t it be nice if your stuff just worked?”</p>
  </section>

  <section class="service svc-managed">
    <div class="service-head">
      <div class="service-icon">
        <svg width="26" height="24" viewBox="0 0 26 24" fill="none" stroke="#333" stroke-width="1.6"><rect x="2" y="2" width="22" height="14" rx="1.5"/><path d="M9 21h8M13 16v5"/></svg>
      </div>
      <h2 class="service-pill">Managed IT Services</h2>
    </div>
    <p class="service-text">Let us take care of your IT. Our MSP is a Flat Rate service that includes Onsite &amp; Remote Support, Endpoint Protection, Web Filtering, Encrypted Online Backup &amp; Patch Management.</p>
  </section>

  <section class="service svc-support">
    <div class="service-head">
      <div class="service-icon">
        <svg width="26" height="26" viewBox="0 0 26 26" fill="none" stroke="#333" stroke-width="1.6"><circle cx="13" cy="13" r="4"/><path d="M13 2v4M13 20v4M2 13h4M20 13h4M5.2 5.2l2.8 2.8M18 18l2.8 2.8M5.2 20.8L8 18M18 8l2.8-2.8"/></svg>
      </div>
      <h2 class="service-pill">IT Support</h2>
    </div>
    <p class="service-text">We have a passion for what we do and it shows! Korvanet provides fast, reliable, expert solutions from experienced staff. You will never feel like just another client to us because our customers are family!</p>
  </section>

  <section class="service svc-voip">
    <div class="service-head">
      <div class="service-icon">
        <svg width="24" height="24" viewBox="0 0 24 24" fill="none" stroke="#333" stroke-width="1.6"><path d="M5 3h4l2 5-2.5 1.5a11 11 0 0 0 6 6L16 13l5 2v4a2 2 0 0 1-2 2A17 17 0 0 1 3 5a2 2 0 0 1 2-2z"/></svg>
      </div>
      <h2 class="service-pill">VOIP Solutions</h2>
    </div>
    <p class="service-text">Phones are more than just an attachment to a desk. Allow us to help you maximize communication with your team and customers by using the latest technology that will likely save you money as well. Korvanet Technologies partners with Relaywave to provide phone hardware, systems, and phone service.</p>
  </section>

  <section class="service svc-wifi">
    <div class="service-head">
      <div class="service-icon">
        <svg width="26" height="24" viewBox="0 0 26 24" fill="none" stroke="#333" stroke-width="1.6"><path d="M4 8a13 13 0 0 1 18 0M7.5 11.5a8 8 0 0 1 11 0M11 15a3 3 0 0 1 4 0"/><circle cx="13" cy="19" r="1.3" fill="#333"/></svg>
      </div>
      <h2 class="service-pill">WiFi Solutions</h2>
    </div>
    <p class="service-text">WiFi is everywhere! (At least it should be.) Korvanet can extend your WiFi to cover your whole campus.</p>
  </section>

  <section class="partners" aria-label="Technology partners">
    <span class="partner">Vantorix</span>
    <span class="partner">Meshline</span>
    <span class="partner">CallHarbor</span>
    <span class="partner">Brightgate Partner</span>
    <span class="partner partner-major">Northwind Partner</span>
    <span class="partner-badge" role="img" aria-label="Partner certification badge"></span>
  </section>

  <footer class="contact-bar">
    <span class="contact-item">
      <svg width="16" height="16" viewBox="0 0 16 16" fill="none" stroke="#fff" stroke-width="1.5"><circle cx="8" cy="8" r="6.5"/><path d="M1.5 8h13M8 1.5c2.5 3 2.5 10 0 13M8 1.5c-2.5 3-2.5 10 0 13"/></svg>
      www.korvanetpro.com
    </span>
    <span class="contact-divider"></span>
    <span class="contact-item">
      <svg width="16" height="16" viewBox="0 0 24 24" fill="none" stroke="#fff" stroke-width="2"><path d="M5 3h4l2 5-2.5 1.5a11 11 0 0 0 6 6L16 13l5 2v4a2 2 0 0 1-2 2A17 17 0 0 1 3 5a2 2 0 0 1 2-2z"/></svg>
      +1 (555) 014-2380
    </span>
    <span class="contact-divider"></span>
    <span class="contact-item">
      <svg width="18" height="14" viewBox="0 0 18 14" fill="none" stroke="#fff" stroke-width="1.5"><rect x="1" y="1" width="16" height="12" rx="1"/><path d="M1 1l8 7 8-7"/></svg>
      hello@korvanetpro.com
    </span>
  </footer>
</main>
</body>
</html>
```